Business Card Design Project

Need a business card design for a new company called StoneWave.

We help large data center customers optimize and transform their data centers.

We have't gotten a logo yet but are in the process of running a separate contest to do that here on ArtHive.

Will post the logo shortly.
Updates

Project Deadline Extended
Reason: Not sure why this came up as a deadline of November 3d. We just launched it today. Going to send an email to ArtHive

Just uploaded larger files of the logo

Target Market(s)

Our target customers of our business are organizations with large data centers looking at optimizing their current data centers, relocating or consolidating their data centers into new data centers.

Typically our buyer will be the CIO, CTO or CFO of the organization.

Industry/Entity Type

Business

Font styles to use
Sans Serif

Colors
3276b5
fece3e

Requirements
Nice to have
• Be readable by the business card reader.
Should not have
• Small type that can't be scanned or easily read
Odd shape or size

```html
<!DOCTYPE html>
<html lang="en">
<head>
<meta charset="utf-8">
<title>StoneWave Business Card</title>
<link rel="stylesheet" href="https://fonts.googleapis.com/css2?family=Ubuntu:wght@400;500&display=swap">
<style>
  :root {
    --page-bg: #e9e7e4;
    --card-light: #d6d2ce;
    --card-mid: #bdb8b3;
    --card-dark: #2c2b2b;
    --band: #242323;
    --ring-light: #ffffff;
    --text-dark: #262626;
    --label-blue: #2a9fd6;
    --name-orange: #e0581c;
    --brand-blue: #3276b5;
    --brand-accent: #ee6a1f;
  }
  html, body {
    margin: 0;
    width: 1200px;
    height: 970px;
    overflow: hidden;
    background: var(--page-bg);
  }
  .canvas {
    position: relative;
    width: 1200px;
    height: 970px;
  }
  .business-card {
    position: absolute;
    left: 100px;
    top: 207px;
    width: 1000px;
    height: 555px;
    box-shadow: 0 18px 40px rgba(0,0,0,0.18);
  }
  .card-art { display: block; }
  .contact-line {
    font-family: "Ubuntu", sans-serif;
    font-size: 19px;
    fill: var(--text-dark);
  }
  .contact-label { fill: var(--label-blue); }
  .holder-name {
    font-family: "Ubuntu", sans-serif;
    font-size: 21px;
    font-weight: 500;
    fill: var(--name-orange);
  }
  .brand-name {
    font-family: "Ubuntu", sans-serif;
    font-size: 60px;
    font-weight: 500;
    fill: var(--brand-blue);
  }
</style>
</head>
<body>
<main class="canvas">
  <section class="business-card" aria-label="StoneWave business card">
    <svg class="card-art" width="1000" height="555" viewBox="0 0 1000 555" xmlns="http://www.w3.org/2000/svg">
      <defs>
        <clipPath id="card-shape"><rect width="1000" height="555"/></clipPath>
        <linearGradient id="frost" x1="0" y1="0" x2="1" y2="1">
          <stop offset="0" stop-color="var(--card-light)"/>
          <stop offset="1" stop-color="var(--card-mid)"/>
        </linearGradient>
        <path id="arc-address" d="M 171 450 A 340 340 0 0 1 346 -45"/>
        <path id="arc-web" d="M 296 513 A 290 290 0 0 1 412 -11"/>
        <path id="arc-mobile" d="M 370 491 A 235 235 0 0 1 442 41"/>
        <path id="arc-name" d="M 334 387 A 170 170 0 0 1 432 108"/>
      </defs>

      <g clip-path="url(#card-shape)">
        <rect class="card-base" width="1000" height="555" fill="url(#frost)"/>
        <rect class="card-dark-edge" x="860" y="0" width="140" height="555" fill="var(--card-dark)"/>

        <g class="rings">
          <circle cx="462" cy="275" r="418" fill="var(--ring-light)" opacity="0.16"/>
          <circle cx="462" cy="275" r="365" fill="var(--card-mid)" opacity="0.55"/>
          <circle cx="462" cy="275" r="365" fill="var(--ring-light)" opacity="0.14"/>
          <circle cx="462" cy="275" r="265" fill="var(--ring-light)" opacity="0.18"/>
          <circle cx="462" cy="275" r="200" fill="var(--card-light)" opacity="0.7"/>
        </g>

        <path class="brand-band" d="M 447 162 H 1000 V 385 H 447 A 111.5 111.5 0 0 1 447 162 Z" fill="var(--band)"/>
      </g>

      <g class="brand-lockup">
        <circle cx="480" cy="273" r="34" fill="var(--brand-accent)"/>
        <text class="brand-name" x="536" y="294">StoneWave</text>
      </g>

      <g class="contact-details">
        <text class="contact-line"><textPath href="#arc-address">Here your company or home address.</textPath></text>
        <text class="contact-line"><textPath href="#arc-web">Mail : info@stonewave.com <tspan class="contact-label" dx="14">Web :</tspan> www.stonewave.com</textPath></text>
        <text class="contact-line"><textPath href="#arc-mobile">Phone : 01 55 5500 0107 <tspan class="contact-label" dx="14">Mobile :</tspan> 200 555 010 20</textPath></text>
        <text class="holder-name"><textPath href="#arc-name">Marlo Penn / CIO</textPath></text>
      </g>
    </svg>
  </section>
</main>
</body>
</html>
```